Design a Website Mockup for VIP Taxi Transfers

Design website mockup for website providing Taxi Transfers (mainly airports transfers).
Company is specialized in Aurelle Transfers and website will be only VIP oriented.

As an example you can have a look at: http://www.pexora-worldwide.example/
We need more trendy design than Pexora Worldwide, but the main point is that the design must say (show) that it is Aurelle Transfers for VIP persons and not ordinary people. So everything must be in luxury format.
1. As a name for the company you can take "Aurelle Transfers" and some dummy slogan (it doesn't matter in this point)
2. We will need simple logo with website mockup
3. Website will be responsive, so you can take that in account
4. The most important message of the design must be "LUXURY", it must be simple and luxurious.
5. Show us two-three pages of the website (e.g. Homepage, Fleet (cars) page, Contact us page, Vobrel Spots page with custom markers (locations where we work).
6. We only need PSD files.

If you will have any further question or clarification, don't hesitate to ask them.
Good Luck!!!

```html
<!DOCTYPE html>
<html lang="en">
<head>
<meta charset="utf-8">
<title>Aurelle Transfers — Travel Refined</title>
<link rel="stylesheet" href="https://fonts.googleapis.com/css2?family=Tinos&display=swap">
<style>
  :root {
    --header-light: #5a5a5a;
    --header-dark: #0e0e0e;
    --gold-text: #ecdca0;
    --bronze: #a9884f;
    --heading: #a2804f;
    --eyebrow: #6f6f6f;
    --rule: #d9d9d9;
    --separator: #2a2a2a;
    --white: #ffffff;
  }
  * { margin: 0; padding: 0; box-sizing: border-box; }
  html, body { width: 1200px; height: 843px; overflow: hidden; background: var(--white); }
  .page { position: relative; width: 1200px; height: 843px; font-family: "Tinos", "Times New Roman", serif; }

  .site-header {
    position: absolute; left: 0; top: 0; width: 1200px; height: 220px;
    background: radial-gradient(ellipse 520px 260px at 600px 90px, var(--header-light), #2a2a2a 60%, var(--header-dark));
  }
  .brand {
    position: absolute; left: 400px; top: 70px; width: 400px; text-align: center;
    color: var(--gold-text); font-size: 24px; line-height: 30px; font-weight: 400; letter-spacing: 1px;
  }

  .main-nav { position: absolute; left: 0; top: 133px; width: 1200px; height: 80px; }
  .main-nav a {
    position: absolute; top: 38px; transform: translateX(-50%);
    color: var(--gold-text); text-decoration: none; font-size: 13px; text-transform: uppercase; white-space: nowrap;
  }
  .nav-sep { position: absolute; top: 0; width: 1px; height: 80px; background: var(--separator); box-shadow: 1px 0 0 #3c3c3c; }

  .gold-band { position: absolute; left: 0; top: 220px; width: 1200px; height: 16px; background: var(--bronze); }

  .eyebrow {
    position: absolute; left: 0; top: 276px; width: 1200px; text-align: center;
    color: var(--eyebrow); font-size: 13px; letter-spacing: 4px; text-transform: uppercase;
  }
  .headline {
    position: absolute; left: 0; top: 312px; width: 1200px; text-align: center;
    color: var(--heading); font-size: 45px; font-weight: 400;
  }
  .divider { position: absolute; top: 419px; height: 4px; border-top: 1px solid var(--rule); border-bottom: 1px solid var(--rule); }
  .divider.left { left: 103px; width: 446px; }
  .divider.right { left: 640px; width: 447px; }
  .divider-mark { position: absolute; left: 575px; top: 410px; width: 40px; height: 22px; background: #e6e6e6; border-radius: 11px; }

  .hero-visual {
    position: absolute; left: 320px; top: 469px; width: 480px; height: 320px;
    background: linear-gradient(180deg, #ffffff 0%, #e9e9ee 35%, #2b2b30 70%, #111114 100%);
  }

  .site-footer {
    position: absolute; left: 0; top: 795px; width: 1200px; height: 48px;
    background: radial-gradient(ellipse 300px 60px at 600px 48px, #4a4a4a, var(--header-dark));
  }
</style>
</head>
<body>
<div class="page">
  <header class="site-header">
    <div class="brand">Aurelle Transfers</div>
    <nav class="main-nav">
      <a href="#" style="left:380px">News</a>
      <span class="nav-sep" style="left:418px"></span>
      <a href="#" style="left:457px">About</a>
      <span class="nav-sep" style="left:496px"></span>
      <a href="#" style="left:543px">Services</a>
      <span class="nav-sep" style="left:588px"></span>
      <a href="#" style="left:633px">Contact</a>
      <span class="nav-sep" style="left:677px"></span>
      <a href="#" style="left:719px">Sample</a>
      <span class="nav-sep" style="left:762px"></span>
      <a href="#" style="left:803px">Sample</a>
    </nav>
  </header>
  <div class="gold-band"></div>

  <main>
    <p class="eyebrow">— Classic Elegance —</p>
    <h1 class="headline">Transfer To The Top of The Class</h1>
    <div class="divider left"></div>
    <div class="divider-mark" role="img" aria-label="Small decorative flourish"></div>
    <div class="divider right"></div>
    <div class="hero-visual" role="img" aria-label="Airliner taking off above a black stretch limousine"></div>
  </main>

  <footer class="site-footer"></footer>
</div>
</body>
</html>
```